Business Card for my New Brokerage

Looking to get a business card design for my new Real Estate Brokerage.
I want it with Picture, Phone Number, Email, Website, Office Address
Name and Designation. Please add logo too.

Target Market(s)

Real Estate Investors or Home Buyers

Industry/Entity Type

Real Estate

Contact Information for Business Card

Name, Email, Phone Number, website, email, office address

Colors
EB3D1F
EC4F4E
F09395
F8D3D4
FCEDEE

Requirements
Must have
• Minimalistic, Clean, Modern, Photo
Nice to have
• White and Red Colors

```html
<!DOCTYPE html>
<html lang="en">
<head>
<meta charset="utf-8">
<title>Ember Realty Inc – Business Card</title>
<link rel="stylesheet" href="https://fonts.googleapis.com/css2?family=Lato:wght@400;900&display=swap">
<style>
  :root {
    --canvas: #2a2a2c;
    --card-dark: #1b1b1d;
    --pattern-dark: #232326;
    --brand-red: #e00000;
    --gold: #d9b25c;
    --gold-light: #f3dc9a;
    --text-light: #ffffff;
    --suit-dark: #2b2b2b;
    --suit-mid: #4a4440;
  }
  * { box-sizing: border-box; margin: 0; padding: 0; }
  html, body { width: 1200px; height: 1108px; overflow: hidden; }
  body {
    background: var(--canvas);
    font-family: "Lato", sans-serif;
    position: relative;
  }
  .card {
    position: absolute;
    top: 214px;
    width: 420px;
    height: 680px;
    border-radius: 22px;
    overflow: hidden;
    background: var(--card-dark);
    box-shadow: 0 18px 40px rgba(0,0,0,0.45);
  }
  .card--front { left: 150px; }
  .card--back { left: 630px; }

  .front-art { position: absolute; left: 0; top: 0; width: 420px; height: 400px; display: block; }

  .holder { position: absolute; left: 0; right: 0; top: 432px; text-align: center; }
  .holder__name {
    color: var(--brand-red);
    font-weight: 900;
    font-size: 30px;
    letter-spacing: 0.5px;
    text-transform: uppercase;
  }
  .holder__role { color: var(--text-light); font-size: 20px; margin-top: 2px; }

  .brand-name {
    position: absolute; left: 0; right: 0;
    text-align: center;
    color: var(--brand-red);
    font-weight: 900;
    font-size: 40px;
    line-height: 1.1;
  }
  .card--front .brand-name { top: 560px; }
  .card--back .brand-name { top: 220px; }

  .back-pattern {
    position: absolute; inset: 0;
    background: radial-gradient(circle at 60% 20%, #2e2e31 0%, var(--pattern-dark) 45%, var(--card-dark) 100%);
  }

  .contact {
    position: absolute; left: 0; right: 0; top: 448px;
    text-align: center; color: var(--text-light); font-size: 21px; line-height: 1.35;
  }
  .contact__divider {
    width: 80px; height: 2px; background: var(--brand-red); margin: 12px auto 10px;
  }
  .contact__label { color: var(--brand-red); font-weight: 900; margin-right: 6px; }
</style>
</head>
<body>
  <section class="card card--front">
    <svg class="front-art" viewBox="0 0 420 400">
      <defs>
        <linearGradient id="portraitTone" x1="0" y1="0" x2="0" y2="1">
          <stop offset="0" stop-color="#6b4a37"/>
          <stop offset="0.45" stop-color="var(--suit-mid)"/>
          <stop offset="1" stop-color="var(--suit-dark)"/>
        </linearGradient>
        <linearGradient id="goldLine" x1="0" x2="1">
          <stop offset="0" stop-color="var(--gold)"/>
          <stop offset="0.5" stop-color="var(--gold-light)"/>
          <stop offset="1" stop-color="var(--gold)"/>
        </linearGradient>
      </defs>
      <rect width="420" height="400" fill="var(--brand-red)"/>
      <rect x="60" y="80" width="330" height="320" rx="40"
            fill="url(#portraitTone)" role="img"
            aria-label="Portrait photo of the managing director in a dark suit and tie"/>
      <path d="M0 312 Q170 410 420 396 L420 400 L0 400 Z" fill="var(--card-dark)"/>
      <path d="M0 312 Q170 410 420 396" fill="none" stroke="url(#goldLine)" stroke-width="4"/>
    </svg>
    <div class="holder">
      <p class="holder__name">Marcus Reed</p>
      <p class="holder__role">Managing Director</p>
    </div>
    <p class="brand-name">Ember Realty Inc</p>
  </section>

  <section class="card card--back">
    <div class="back-pattern" role="img" aria-label="Subtle dark decorative pattern background"></div>
    <p class="brand-name">Ember Realty Inc</p>
    <div class="contact">
      <p>88 Harbor Lane</p>
      <p>Westfield, 20418</p>
      <div class="contact__divider"></div>
      <p><span class="contact__label">P:</span>044-987 654 321</p>
      <p><span class="contact__label">E:</span>hello@emberrealty.com</p>
      <p><span class="contact__label">W:</span>www.emberrealty.com</p>
    </div>
  </section>
</body>
</html>
```